International gym review site. Needs a full website frontend (mobile + desktop) designing and a logo

Our UK based business 'LiftHarbor' is launching its international review website for independent and hotel gyms. Our website will be a fresh, funky and clean version of Wanderquill but for gyms.
We require the designs in sketch, psd, illustrator

We would like to see clean designs that incorporate gym style icons. We also require our logo designing which will need to complement the design of the site. We have included wireframes of how we envisage the site coming together. However, we are very flexible on this and have nothing set in stone.

We would like the designs to mobile first focused with desktop experince being the latter (although we have wireframed for desktop - we are very open to ideas and suggestions)

Please find below a number of websites that we like and have found inspiration from:

- https://www.bookvane.example/uk/
- chatterloom.example
- Map is cool on here https://bigroster.bypilotcraft.example/
- Looks cool like nest n'go (listing section could be smaller) -https://tintforge.example/demos/themes/?product=rowable
- Like this but needs to be more compact https://rowkit-demos.brimfold.example/rentals/listing/private-bedroom-w-bathroom/
- Like the homepage of this one https://rankhop.venmora.example/
- https://www.paddlo.example.co.uk/hotels - looks clean, like the layout of this especially the hotel section
- https://www.paddlo.example.co.uk/Barcelona-Hotels.48213.hotel.ksp - the good to know section is good
- https://chipwire.example/2017/10/20/flickcast-unveils-a-suite-of-new-tools-to-help-creators-grow-their-channels-and-make-money/
- https://www.quietlodging.example/
- https://www.wheelmarket.example.co.uk

Target Market(s)

Fitness users and hotel goers who want to use a gym. Generally affluent aged 20-50years old of multi-nationalities

Industry/Entity Type

Fitness

Logo Text

LiftHarbor (optional)

Number of Pages Required

5+ page

Colors

Designer to choose colors to be used in the design.

Requirements
Must have
• Clean, flat minimal, pleasing on the eye.
• Bright / colourful
• Clean fonts (no specific font picked, will leave colour palette and fonts to the designer)
Should not have
• Cluttered and disorganised feel.
• Dark and dreary.

```html
<!DOCTYPE html>
<html lang="en">
<head>
<meta charset="utf-8">
<title>LiftHarbor – Independent and Hotel Gyms</title>
<link href="https://fonts.googleapis.com/css2?family=Montserrat:wght@600;700;800;900&family=Open+Sans:wght@400;600;700&display=swap" rel="stylesheet">
<style>
:root{
  --blue:#1a7cf4;
  --blue-dark:#0f5fc8;
  --blue-soft:#dbe9fb;
  --navy:#10243f;
  --ink:#1d1d1f;
  --muted:#7b7f86;
  --grey-bg:#f1f2f4;
  --skin:#f2b48c;
  --footer:#141414;
  --footer-bottom:#0b0b0b;
  --white:#ffffff;
}
*{margin:0;padding:0;box-sizing:border-box}
html,body{width:1200px;height:3688px;overflow:hidden;background:var(--white)}
body{font-family:'Open Sans',Arial,sans-serif;color:var(--ink);font-size:14px;line-height:1.6}
h1,h2,h3,h4{font-family:'Montserrat',Arial,sans-serif}

/* header */
.site-header{position:relative;height:104px;background:var(--white)}
.brand{position:absolute;left:236px;top:10px;width:88px;text-align:center}
.brand-mark{width:44px;height:44px;border-radius:50%;border:3px solid var(--ink);margin:0 auto 6px}
.brand-name{font-family:'Montserrat',sans-serif;font-weight:700;font-size:13px;color:var(--ink)}
.topbar{position:absolute;left:388px;top:0;width:592px;height:48px;display:flex;gap:36px;align-items:center;font-size:11px;color:var(--muted);white-space:nowrap}
.topbar .socials{margin-left:auto;display:flex;gap:8px}
.socials span{width:20px;height:20px;border-radius:50%;background:var(--blue);display:block}
.nav{position:absolute;left:388px;width:592px;top:48px;height:44px;background:var(--blue);display:flex;align-items:center;padding:0 18px;gap:18px}
.nav a{color:var(--white);font-family:'Montserrat',sans-serif;font-size:10px;font-weight:700;text-decoration:none;text-transform:uppercase;white-space:nowrap}
.nav .search{margin-left:auto;width:100px;height:24px;background:var(--white);border-radius:2px;font-size:10px;color:var(--muted);padding:4px 10px}

/* hero */
.hero{position:relative;height:536px;overflow:hidden}
.hero .photo{position:absolute;inset:0;background:
  radial-gradient(ellipse 420px 320px at 980px 240px,rgba(230,236,242,.55),transparent 70%),
  linear-gradient(90deg,#1d3e6c 0%,#35598a 40%,#7d8893 75%,#aeb4ba 100%)}
.hero-copy{position:absolute;left:248px;top:176px;width:520px;color:var(--white)}
.hero h1{font-size:46px;font-weight:800;line-height:1.1;text-transform:uppercase}
.hero p{margin-top:16px;font-size:17px;line-height:1.45;color:#d9e6ff}
.btn{display:inline-block;background:var(--blue);color:var(--white);font-family:'Montserrat',sans-serif;font-size:11px;font-weight:700;text-transform:uppercase;padding:12px 26px;border-radius:2px}
.btn-light{background:var(--white);color:var(--blue)}
.hero .btn{margin-top:28px;background:var(--white);color:var(--blue)}

/* about */
.about{position:relative;height:408px;overflow:hidden}
.about-copy{position:absolute;left:100px;top:44px;width:450px;z-index:1}
.about h2{font-size:34px;font-weight:800;color:var(--blue);text-transform:uppercase}
.about .lead{font-size:13px;color:var(--muted);margin-top:6px}
.about .body{font-size:11px;color:var(--muted);margin-top:12px;line-height:1.75}
.about .btn{margin-top:20px}
.about .ghost{position:absolute;left:96px;bottom:6px;font-family:'Montserrat',sans-serif;font-size:78px;font-weight:900;color:#f0f1f3;line-height:1;white-space:nowrap}
.about .photo{position:absolute;left:592px;top:0;width:608px;height:408px;background:
  radial-gradient(ellipse 260px 120px at 380px 60px,rgba(214,236,240,.7),transparent 70%),
  linear-gradient(180deg,#c9d6dc 0%,#8c8f93 45%,#5b4a3e 72%,#b9864f 100%)}

/* section titles */
.section-title{text-align:center;font-size:34px;font-weight:800;color:var(--blue);text-transform:uppercase}
.divider{display:block;margin:14px auto 0}

/* hotel gym */
.hotel-gym{height:512px;padding-top:72px}
.feature-row{display:flex;justify-content:center;gap:72px;margin-top:52px}
.feature{width:176px;text-align:center}
.feature .icon{width:124px;height:124px;border-radius:50%;background:radial-gradient(circle,#e4eefb 0,#f1f6fc 70%);margin:0 auto;display:flex;align-items:center;justify-content:center}
.feature h3{font-size:13px;font-weight:800;margin-top:30px;text-transform:uppercase}
.feature p{font-size:11px;color:var(--muted);margin-top:8px;line-height:1.55}

/* independent gym */
.independent-gym{height:532px;background:var(--grey-bg);padding-top:60px}
.card-row{display:flex;justify-content:center;gap:28px;margin-top:50px}
.gym-card{width:344px;text-align:center}
.gym-card .photo{height:204px}
.gym-card h3{font-size:14px;font-weight:800;margin-top:22px;text-transform:uppercase}
.gym-card p{font-size:11px;color:var(--muted);margin-top:6px;line-height:1.55}

/* promo band */
.promo{height:348px;background:linear-gradient(90deg,#1677ee,#2a89fa);text-align:center;color:var(--white);padding-top:80px}
.promo h2{font-size:36px;font-weight:800;text-transform:uppercase}
.promo p{font-size:19px;width:680px;margin:14px auto 0;line-height:1.45}
.promo .btn{margin-top:28px}

/* events */
.events{height:620px;padding-top:64px}
.events .section-title{font-size:38px}
.event-row{display:flex;justify-content:center;gap:16px;margin-top:58px}
.event-card{width:232px;height:360px;position:relative;background:var(--navy)}
.event-card .date{height:30px;background:var(--blue);color:var(--white);font-family:'Montserrat',sans-serif;font-size:12px;font-weight:700;padding:6px 12px;text-transform:uppercase}
.event-card .photo{position:absolute;top:30px;left:0;right:0;bottom:0}
.event-card .caption{position:absolute;left:0;right:0;bottom:0;background:rgba(20,110,230,.85);color:var(--white);padding:14px 14px 16px}
.event-card h4{font-size:13px;font-weight:800;text-transform:uppercase}
.event-card p{font-size:10px;line-height:1.5;margin-top:4px}

/* newsletter */
.newsletter{height:280px;padding-top:42px}
.subscribe{width:480px;height:46px;margin:44px auto 0;border:1px solid #e0e2e6;display:flex;align-items:center;padding-left:16px}
.subscribe span{font-size:11px;color:#aaa;flex:1}
.subscribe b{font-family:'Montserrat',sans-serif;font-size:11px;color:var(--blue);padding:0 24px}

/* footer */
.site-footer{height:308px;background:var(--footer);color:#bfc2c6;position:relative}
.footer-cols{position:absolute;left:248px;top:36px;display:flex}
.footer-col h4{color:var(--white);font-size:12px;font-weight:800;text-transform:uppercase;margin-bottom:14px}
.footer-col p,.footer-col li{font-size:10px;line-height:1.7}
.footer-col ul{list-style:none}
.footer-col li{margin-bottom:10px}
.footer-col li::before{content:"›";color:var(--blue);margin-right:6px}
.col-info{width:220px;padding-right:24px}
.col-gyms{width:172px}
.col-links{width:112px}
.col-contact{width:248px}
.field{height:30px;background:#1f1f1f;border:1px solid #2c2c2c;margin-bottom:10px;font-size:10px;color:#777;padding:6px 10px}
.field.tall{height:68px}
.send{display:inline-block;background:var(--blue);color:var(--white);font-size:10px;font-weight:700;padding:5px 16px}
.footer-bottom{position:absolute;left:0;right:0;bottom:0;height:40px;background:var(--footer-bottom);color:#8b8f94;font-size:10px;display:flex;justify-content:space-between;align-items:center;padding:0 248px}
</style>
</head>
<body>

<header class="site-header">
  <div class="brand"><div class="brand-mark"></div><div class="brand-name">LiftHarbor</div></div>
  <div class="topbar">
    <span>Phone: +44 (0)20 7946 0137</span>
    <span>Email: hello@liftharbor.example</span>
    <div class="socials"><span></span><span></span><span></span><span></span></div>
  </div>
  <nav class="nav">
    <a>Home</a><a>About Us</a><a>Hotel Gym</a><a>Independent</a><a>Events</a><a>Blog</a><a>Contact Us</a>
    <div class="search">Search</div>
  </nav>
</header>

<section class="hero">
  <div class="photo" role="img" aria-label="Man training with a dumbbell in a bright gym"></div>
  <div class="hero-copy">
    <h1>Independent<br>and Hotel Gyms</h1>
    <p>Lorem Ipsum is simply dummy text of the printing and typesetting industry. Lorem Ipsum has been the industry's</p>
    <span class="btn">Read More</span>
  </div>
</section>

<section class="about">
  <div class="ghost" aria-hidden="true">ABOUT US</div>
  <div class="about-copy">
    <h2>About Us</h2>
    <p class="lead">Lorem Ipsum is simply dummy text of the printing and typesetting industry. Lorem Ipsum has been the industry's</p>
    <p class="body">Lorem Ipsum is simply dummy text of the printing and typesetting industry. Lorem Ipsum has been the industry's standard dummy text ever since the 1500s, when an unknown printer took a galley of type and scrambled it to make a type specimen book. It has survived not only five centuries, but also the leap into electronic typesetting, remaining essentially unchanged. It was popularised in the 1960s with the release of sheets containing passages.</p>
    <span class="btn">Read More</span>
  </div>
  <div class="photo" role="img" aria-label="Gym floor with treadmills and weight machines"></div>
</section>

<section class="hotel-gym">
  <h2 class="section-title">Hotel Gym</h2>
  <svg class="divider" width="40" height="14" viewBox="0 0 40 14"><rect x="2" y="2" width="4" height="10" fill="#1a7cf4"/><rect x="7" y="4" width="3" height="6" fill="#1a7cf4"/><rect x="10" y="6" width="20" height="2" fill="#1a7cf4"/><rect x="30" y="4" width="3" height="6" fill="#1a7cf4"/><rect x="34" y="2" width="4" height="10" fill="#1a7cf4"/></svg>
  <div class="feature-row">
    <div class="feature">
      <div class="icon" role="img" aria-label="Weightlifting icon">
        <svg width="72" height="72" viewBox="0 0 72 72"><rect x="6" y="24" width="8" height="24" rx="2" fill="#1a7cf4"/><rect x="14" y="28" width="6" height="16" rx="2" fill="#0f5fc8"/><rect x="20" y="33" width="32" height="6" fill="#4a5562"/><rect x="52" y="28" width="6" height="16" rx="2" fill="#0f5fc8"/><rect x="58" y="24" width="8" height="24" rx="2" fill="#1a7cf4"/></svg>
      </div>
      <h3>Weightlifting</h3><p>Lorem Ipsum is simply dummy text of the printing and typesetting industry. Lorem Ipsum has been the industry's</p>
    </div>
    <div class="feature">
      <div class="icon" role="img" aria-label="Cycling icon">
        <svg width="76" height="72" viewBox="0 0 76 72"><circle cx="18" cy="46" r="13" fill="none" stroke="#4a5562" stroke-width="4"/><circle cx="58" cy="46" r="13" fill="none" stroke="#4a5562" stroke-width="4"/><path d="M18 46 L32 24 L50 24 L58 46 M32 24 L40 46 L50 24" fill="none" stroke="#1a7cf4" stroke-width="4" stroke-linejoin="round"/><rect x="26" y="18" width="12" height="4" rx="2" fill="#0f5fc8"/></svg>
      </div>
      <h3>Cycling</h3><p>Lorem Ipsum is simply dummy text of the printing and typesetting industry. Lorem Ipsum has been the industry's</p>
    </div>
    <div class="feature">
      <div class="icon" role="img" aria-label="Body work icon">
        <svg width="72" height="72" viewBox="0 0 72 72"><path d="M28 12 L28 44 L12 44 L12 58 L60 58 L60 44 L44 44 L44 12 Z" fill="#1a7cf4"/><rect x="22" y="8" width="28" height="8" rx="3" fill="#0f5fc8"/><rect x="8" y="56" width="56" height="6" rx="3" fill="#4a5562"/></svg>
      </div>
      <h3>Body Work</h3><p>Lorem Ipsum is simply dummy text of the printing and typesetting industry. Lorem Ipsum has been the industry's</p>
    </div>
  </div>
</section>

<section class="independent-gym">
  <h2 class="section-title">Independent Gym</h2>
  <svg class="divider" width="40" height="14" viewBox="0 0 40 14"><rect x="2" y="2" width="4" height="10" fill="#1a7cf4"/><rect x="7" y="4" width="3" height="6" fill="#1a7cf4"/><rect x="10" y="6" width="20" height="2" fill="#1a7cf4"/><rect x="30" y="4" width="3" height="6" fill="#1a7cf4"/><rect x="34" y="2" width="4" height="10" fill="#1a7cf4"/></svg>
  <div class="card-row">
    <div class="gym-card"><div class="photo" role="img" aria-label="Kettlebells lined up on a gym floor" style="background:linear-gradient(180deg,#d9dcdf 0%,#9aa0a6 50%,#3a3d41 100%)"></div><h3>Kettlebell Power</h3><p>Lorem Ipsum is simply dummy text of the printing and typesetting industry. Lorem Ipsum has been the industry's</p></div>
    <div class="gym-card"><div class="photo" role="img" aria-label="Athlete doing a core exercise" style="background:linear-gradient(180deg,#e6e8ea 0%,#b5bcc4 45%,#2f4d78 100%)"></div><h3>Core Power</h3><p>Lorem Ipsum is simply dummy text of the printing and typesetting industry. Lorem Ipsum has been the industry's</p></div>
    <div class="gym-card"><div class="photo" role="img" aria-label="Runner on a treadmill" style="background:linear-gradient(135deg,#2f3338 0%,#6b747e 55%,#a7b4c0 100%)"></div><h3>Running</h3><p>Lorem Ipsum is simply dummy text of the printing and typesetting industry. Lorem Ipsum has been the industry's</p></div>
  </div>
</section>

<section class="promo">
  <h2>Independent and Hotel Gyms</h2>
  <p>Lorem Ipsum is simply dummy text of the printing and typesetting industry. Lorem Ipsum has been the industry's</p>
  <span class="btn btn-light">Visit Us</span>
</section>

<section class="events">
  <h2 class="section-title">Events</h2>
  <svg class="divider" width="40" height="14" viewBox="0 0 40 14"><rect x="2" y="2" width="4" height="10" fill="#1a7cf4"/><rect x="7" y="4" width="3" height="6" fill="#1a7cf4"/><rect x="10" y="6" width="20" height="2" fill="#1a7cf4"/><rect x="30" y="4" width="3" height="6" fill="#1a7cf4"/><rect x="34" y="2" width="4" height="10" fill="#1a7cf4"/></svg>
  <div class="event-row">
    <div class="event-card"><div class="date">28 March 2018</div><div class="photo" role="img" aria-label="City tower blocks against a blue sky" style="background:linear-gradient(160deg,#2f6fb8 0%,#7fb0df 50%,#d7e6f2 100%)"></div><div class="caption"><h4>Lorem Ipsum is simply</h4><p>Lorem Ipsum is simply dummy text of the printing and typesetting industry.</p></div></div>
    <div class="event-card"><div class="date">19 March 2018</div><div class="photo" role="img" aria-label="Rack of weight plates in a gym" style="background:linear-gradient(180deg,#cfd3d7 0%,#5a6068 45%,#1e2226 100%)"></div><div class="caption"><h4>Lorem Ipsum is simply</h4><p>Lorem Ipsum is simply dummy text of the printing and typesetting industry.</p></div></div>
    <div class="event-card"><div class="date">20 March 2018</div><div class="photo" role="img" aria-label="Gym member lifting a barbell" style="background:linear-gradient(180deg,#eceef0 0%,#9aa1a8 50%,#4a4f55 100%)"></div><div class="caption"><h4>Lorem Ipsum is simply</h4><p>Lorem Ipsum is simply dummy text of the printing and typesetting industry.</p></div></div>
    <div class="event-card"><div class="date">28 March 2018</div><div class="photo" role="img" aria-label="Modern city buildings at daytime" style="background:linear-gradient(180deg,#6ea4da 0%,#bcd4ea 50%,#8f9ba6 100%)"></div><div class="caption"><h4>Lorem Ipsum is simply</h4><p>Lorem Ipsum is simply dummy text of the printing and typesetting industry.</p></div></div>
  </div>
</section>

<section class="newsletter">
  <h2 class="section-title">Subscribe to Newsletters</h2>
  <svg class="divider" width="40" height="14" viewBox="0 0 40 14"><rect x="2" y="2" width="4" height="10" fill="#1a7cf4"/><rect x="7" y="4" width="3" height="6" fill="#1a7cf4"/><rect x="10" y="6" width="20" height="2" fill="#1a7cf4"/><rect x="30" y="4" width="3" height="6" fill="#1a7cf4"/><rect x="34" y="2" width="4" height="10" fill="#1a7cf4"/></svg>
  <div class="subscribe"><span>Enter your email</span><b>SUBSCRIBE</b></div>
</section>

<footer class="site-footer">
  <div class="footer-cols">
    <div class="footer-col col-info">
      <h4>Information</h4>
      <p>Find trusted reviews of hotel and independent gyms in cities around the world.</p>
      <p style="margin-top:8px">Address:<br>48 Quayside Row, London</p>
      <p style="margin-top:8px">Phone: +44 (0)20 7946 0137</p>
      <p>Email: hello@liftharbor.example</p>
    </div>
    <div class="footer-col col-gyms">
      <h4>Independent Gym</h4>
      <ul><li>Kettlebell Power</li><li>Core Power</li><li>Running</li><li>Cycling</li></ul>
    </div>
    <div class="footer-col col-links">
      <h4>Quick Link</h4>
      <ul><li>Home</li><li>About Us</li><li>Hotel Gym</li><li>Events</li><li>Contact Us</li></ul>
    </div>
    <div class="footer-col col-contact">
      <h4>Contact Us</h4>
      <div class="field">Name</div>
      <div class="field">Email</div>
      <div class="field tall">Message</div>
      <span class="send">Send</span>
    </div>
  </div>
  <div class="footer-bottom"><span>Copyright © 2018 LiftHarbor. All Rights Reserved.</span><span>Design and development by LiftHarbor Studio</span></div>
</footer>

</body>
</html>
```